Business Strategy Company
Cards & Paper for Enterprise Collaboration Data Company
Project: Business Strategy Company
Business Strategy Company -
Creative Brief
Professional
Tobin G. Maraselt
CEO
31927 Harrowgate Ave. Suite 400 Berkley, CA 90388
tobin@quandelrox.example
www.quandelrox.example
Please include tagline: "Collaboration Intelligence" We would like a clean, modern card like the types found in these designs: https://www.pendlewick.example/drafts/display/contest/93587/draft/705568 https://www.pendlewick.example/drafts/display/contest/79787/draft/600578 https://www.pendlewick.example/drafts/display/contest/77433/draft/650842 https://www.pendlewick.example/drafts/display/contest/50102/draft/406651 https://www.pendlewick.example/drafts/display/contest/101628/draft/769948 https://www.pendlewick.example/drafts/display/contest/101641/draft/771307 https://www.pendlewick.example/drafts/display/contest/99022/draft/771303
We like a field of dark color or a gradient with the logo in either white or a color just slightly lighter/darker than the background (i.e. if the background is black, the logo would either be white or very dark gray). We'd like to see both.

```html
<!DOCTYPE html>
<html lang="en">
<head>
<meta charset="utf-8">
<title>Quandelrox business cards</title>
<link href="https://fonts.googleapis.com/css2?family=Roboto:wght@300;400;700&display=swap" rel="stylesheet">
<style>
  :root {
    --bg: #e9e9ea;
    --paper: #ffffff;
    --ink: #2b2d33;
    --muted: #6a6d75;
    --navy: #24235a;
    --navy-tone: #3a3980;
    --black: #0c0c0d;
    --black-tone: #2c2c30;
    --cyan: #29abe2;
    --deep: #2e3170;
    --slate: #7d8494;
    --band: #dfe3ea;
  }
  * { margin: 0; padding: 0; box-sizing: border-box; }
  html, body { width: 1200px; height: 799px; overflow: hidden; }
  body { background: var(--bg); font-family: "Roboto", sans-serif; position: relative; }

  .card {
    position: absolute; width: 324px; height: 188px; border-radius: 14px;
    overflow: hidden; box-shadow: 0 3px 8px rgba(0,0,0,.18);
  }
  .card--light { background: var(--paper); color: var(--ink); }
  .card--black { background: var(--black); color: #fff; }
  .card--navy { background: var(--navy); color: #fff; }

  .brand { position: absolute; }
  .brand__name { display: flex; align-items: center; gap: 8px; font-size: 24px;
    font-weight: 400; letter-spacing: .5px; color: var(--deep); line-height: 1; }
  .brand__mark { width: 14px; height: 14px; background: var(--cyan); border-radius: 2px; flex: none; }
  .brand__tagline { font-size: 7px; font-weight: 400; letter-spacing: 1.2px;
    text-transform: uppercase; color: var(--muted); margin: 5px 0 0 22px; }

  .person { position: absolute; }
  .person__name { font-size: 11px; font-weight: 700; }
  .person__role { font-size: 8px; color: var(--muted); margin-top: 1px; }

  .contact { position: absolute; font-size: 6.5px; line-height: 9px; color: var(--muted); list-style: none; }
  .contact li { display: flex; gap: 4px; align-items: flex-start; }
  .contact li::before { content: ""; width: 4px; height: 4px; margin-top: 2px; border-radius: 50%; background: var(--deep); flex: none; }
  .contact .gap { margin-top: 4px; }

  .footer { position: absolute; left: 0; right: 0; bottom: 0; height: 15px;
    background: var(--band); font-size: 6px; color: var(--muted); }
  .footer__url { position: absolute; left: 0; right: 0; top: 4px; text-align: center; }
  .footer__swatches { position: absolute; right: 0; top: -5px; display: flex; }
  .footer__swatches span { width: 12px; height: 20px; }
  .sw-cyan { background: var(--cyan); } .sw-deep { background: var(--deep); }
  .sw-slate { background: var(--slate); } .sw-dark { background: #2b2d33; }

  .back-brand { position: absolute; left: 0; right: 0; top: 70px; text-align: center; }
  .back-brand__name { display: inline-flex; align-items: center; gap: 10px;
    font-size: 28px; font-weight: 300; letter-spacing: 1px; line-height: 1; color: #fff; }
  .back-brand .brand__mark { width: 16px; height: 16px; background: #fff; }
  .back-brand__tagline { font-size: 7px; letter-spacing: 1.6px; text-transform: uppercase;
    color: #c9cad6; margin-top: 7px; }
  .back-url { position: absolute; left: 22px; bottom: 10px; font-size: 6px; color: #c9cad6; }

  .card--black.card--tonal .back-brand__name { color: var(--black-tone); }
  .card--black.card--tonal .brand__mark { background: var(--black-tone); }
  .card--black.card--tonal .back-brand__tagline { color: var(--black-tone); }
  .card--navy.card--tonal .back-brand__name { color: var(--navy-tone); }
  .card--navy.card--tonal .brand__mark { background: var(--navy-tone); }
  .card--navy.card--tonal .back-brand__tagline { color: var(--navy-tone); }
</style>
</head>
<body>

<section class="card card--light" style="left:108px; top:137px;">
  <div class="brand" style="left:30px; top:40px;">
    <p class="brand__name"><span class="brand__mark"></span>quandelrox</p>
    <p class="brand__tagline">Collaboration Intelligence</p>
  </div>
  <div class="person" style="left:30px; top:104px;">
    <p class="person__name">Tobin G. Maraselt</p>
    <p class="person__role">CEO</p>
  </div>
  <ul class="contact" style="left:176px; top:98px;">
    <li>31927 Harrowgate Ave. Suite 400<br>Berkley, CA 90388</li>
    <li class="gap">410-555-0142</li>
    <li>213-555-0187</li>
    <li>888-555-0163</li>
    <li>tobin@quandelrox.example</li>
  </ul>
  <footer class="footer"><span class="footer__url">www.quandelrox.example</span>
    <div class="footer__swatches"><span class="sw-cyan"></span><span class="sw-deep"></span><span class="sw-slate"></span><span class="sw-dark"></span></div></footer>
</section>

<section class="card card--light" style="left:456px; top:137px;">
  <div class="brand" style="left:20px; top:82px;">
    <p class="brand__name"><span class="brand__mark"></span>quandelrox</p>
    <p class="brand__tagline">Collaboration Intelligence</p>
  </div>
  <div class="person" style="left:180px; top:36px;">
    <p class="person__name">Tobin G. Maraselt</p>
    <p class="person__role">CEO</p>
  </div>
  <ul class="contact" style="left:180px; top:66px;">
    <li>31927 Harrowgate Ave. Suite 400<br>Berkley, CA 90388</li>
    <li class="gap">410-555-0142</li>
    <li>213-555-0187</li>
    <li>888-555-0163</li>
    <li>tobin@quandelrox.example</li>
  </ul>
  <footer class="footer"><span class="footer__url">www.quandelrox.example</span>
    <div class="footer__swatches"><span class="sw-cyan"></span><span class="sw-deep"></span><span class="sw-slate"></span><span class="sw-dark"></span></div></footer>
</section>

<section class="card card--light" style="left:804px; top:137px;">
  <div class="brand" style="left:18px; top:78px;">
    <p class="brand__name"><span class="brand__mark"></span>quandelrox</p>
    <p class="brand__tagline">Collaboration Intelligence</p>
  </div>
  <div class="person" style="left:184px; top:36px;">
    <p class="person__name">Tobin G. Maraselt</p>
    <p class="person__role">CEO</p>
  </div>
  <ul class="contact" style="left:184px; top:66px;">
    <li>31927 Harrowgate Ave. Suite 400<br>Berkley, CA 90388</li>
    <li class="gap">410-555-0142</li>
    <li>213-555-0187</li>
    <li>888-555-0163</li>
    <li>tobin@quandelrox.example</li>
  </ul>
  <footer class="footer"><span class="footer__url">www.quandelrox.example</span>
    <div class="footer__swatches"><span class="sw-cyan"></span><span class="sw-deep"></span><span class="sw-slate"></span><span class="sw-dark"></span></div></footer>
</section>

<section class="card card--black" style="left:269px; top:345px;">
  <div class="back-brand">
    <p class="back-brand__name"><span class="brand__mark"></span>quandelrox</p>
    <p class="back-brand__tagline">Collaboration Intelligence</p>
  </div>
  <p class="back-url">www.quandelrox.example</p>
</section>
<section class="card card--black card--tonal" style="left:624px; top:345px;">
  <div class="back-brand">
    <p class="back-brand__name"><span class="brand__mark"></span>quandelrox</p>
    <p class="back-brand__tagline">Collaboration Intelligence</p>
  </div>
</section>

<section class="card card--navy" style="left:269px; top:549px;">
  <div class="back-brand">
    <p class="back-brand__name"><span class="brand__mark"></span>quandelrox</p>
    <p class="back-brand__tagline">Collaboration Intelligence</p>
  </div>
  <p class="back-url">www.quandelrox.example</p>
</section>
<section class="card card--navy card--tonal" style="left:624px; top:549px;">
  <div class="back-brand">
    <p class="back-brand__name"><span class="brand__mark"></span>quandelrox</p>
    <p class="back-brand__tagline">Collaboration Intelligence</p>
  </div>
</section>

</body>
</html>
```